Baby Food product, packaging design

Tot Harvest is a home-made style, frozen baby food service. The business provides frozen puree and textured baby food blends in ice-cube like freezer trays.

I am after 9 designs to be used as my front of package sticker, this will include the product name, logo, nutritional panel and other things as per the uploaded document.

***On my document I forgot to add that the second container is 9cm in width (Across) and 13cm in length (down).

```html
<!DOCTYPE html>
<html lang="en">
<head>
<meta charset="utf-8">
<title>Tot Harvest – Sunny Medley Label</title>
<link rel="stylesheet" href="https://fonts.googleapis.com/css2?family=Itim&family=Open+Sans:wght@600;700;800&display=swap">
<style>
  :root {
    --green: #2fb56b;
    --sky: #1e9fe0;
    --step-blue: #5cc7d5;
    --pink: #d8978c;
    --pink-light: #e7b3a8;
    --lime: #dfe0a4;
    --panel: #e6e6e8;
    --ink: #222222;
    --grey: #8a8a8a;
    --red: #d42424;
    --white: #ffffff;
  }
  * { box-sizing: border-box; margin: 0; padding: 0; }
  html, body { width: 1200px; height: 1200px; overflow: hidden; background: var(--white); }
  .canvas { position: relative; width: 900px; height: 900px; transform: scale(1.33334); transform-origin: 0 0; }
  .backdrop { position: absolute; inset: 0; width: 900px; height: 900px; }
  .t { position: absolute; white-space: nowrap; }
  .brand-name { left: 104px; top: 218px; width: 266px; text-align: center; font-family: "Itim", cursive; font-size: 31px; color: #f3f0c8; letter-spacing: 1px; }
  .instructions-title { left: 74px; top: 372px; font-family: "Itim", cursive; font-size: 40px; color: #333; }
  .step-text { left: 167px; font-family: "Itim", cursive; font-size: 20px; line-height: 32px; color: var(--white); }
  .step-num { width: 40px; text-align: center; font-family: "Open Sans", sans-serif; font-weight: 800; font-size: 30px; color: var(--white); }
  .product-name { left: 463px; top: 108px; width: 327px; text-align: center; font-family: "Open Sans", sans-serif; font-weight: 700; font-size: 35px; color: var(--white); }
  .ingredients { left: 430px; top: 190px; width: 405px; text-align: center; font-family: "Open Sans", sans-serif; font-weight: 700; font-size: 22px; line-height: 28px; color: var(--sky); }
  .nutrition-heading { left: 531px; top: 266px; font-family: "Open Sans", sans-serif; font-weight: 700; font-size: 15px; color: var(--green); }
  .nutrition-sub { left: 531px; font-family: "Open Sans", sans-serif; font-weight: 700; font-size: 9px; color: var(--green); }
  .table-label { font-family: "Open Sans", sans-serif; font-weight: 700; font-size: 13px; line-height: 17px; color: var(--green); }
  .storage { left: 555px; top: 719px; width: 198px; text-align: center; font-family: "Open Sans", sans-serif; font-weight: 700; font-size: 13px; color: var(--ink); }
  .allergen { left: 440px; top: 752px; width: 385px; text-align: center; font-family: "Open Sans", sans-serif; font-weight: 700; font-size: 12px; line-height: 18px; color: var(--red); }
  .claims { left: 440px; top: 797px; width: 385px; text-align: center; font-family: "Open Sans", sans-serif; font-weight: 700; font-size: 12px; line-height: 18px; color: var(--grey); }
</style>
</head>
<body>
<div class="canvas">
  <svg class="backdrop" viewBox="0 0 900 900" aria-hidden="false">
    <defs>
      <linearGradient id="pinkFade" x1="0" y1="0" x2="1" y2="0">
        <stop offset="0" stop-color="#d58f85"/>
        <stop offset="1" stop-color="#e9bdb2"/>
      </linearGradient>
      <linearGradient id="bannerFade" x1="0" y1="0" x2="1" y2="0">
        <stop offset="0" stop-color="#d88f84"/>
        <stop offset="1" stop-color="#e6b4aa"/>
      </linearGradient>
      <linearGradient id="harvestTones" x1="0" y1="0" x2="1" y2="0">
        <stop offset="0" stop-color="#f08a3c"/>
        <stop offset="0.3" stop-color="#d6342c"/>
        <stop offset="0.5" stop-color="#8a4a34"/>
        <stop offset="0.7" stop-color="#f5a623"/>
        <stop offset="1" stop-color="#8d2b4f"/>
      </linearGradient>
    </defs>

    <!-- left panel -->
    <rect class="panel-left" x="55" y="55" width="373" height="790" fill="var(--lime)"/>
    <polygon class="panel-left-band" points="140,55 428,55 428,268 55,100 55,55" fill="url(#pinkFade)"/>
    <polygon class="panel-left-wedge" points="55,625 330,845 55,845" fill="url(#pinkFade)"/>

    <!-- right panel -->
    <rect class="panel-right" x="428" y="55" width="417" height="790" fill="var(--panel)"/>

    <!-- brand badge -->
    <circle cx="237" cy="213" r="133" fill="var(--green)"/>
    <circle cx="237" cy="213" r="117" fill="none" stroke="var(--white)" stroke-width="2"/>

    <!-- instruction steps -->
    <g class="step">
      <polygon points="428,527 440,527 428,540" fill="#555"/>
      <rect x="140" y="447" width="300" height="80" fill="url(#bannerFade)"/>
      <circle cx="105" cy="487" r="45" fill="var(--green)"/>
      <circle cx="105" cy="487" r="33" fill="var(--step-blue)"/>
    </g>
    <g class="step">
      <polygon points="428,648 440,648 428,661" fill="#555"/>
      <rect x="140" y="566" width="300" height="82" fill="url(#bannerFade)"/>
      <circle cx="105" cy="607" r="45" fill="var(--green)"/>
      <circle cx="105" cy="607" r="33" fill="var(--step-blue)"/>
    </g>
    <g class="step">
      <polygon points="428,767 440,767 428,780" fill="#555"/>
      <rect x="140" y="685" width="300" height="82" fill="url(#bannerFade)"/>
      <circle cx="105" cy="727" r="45" fill="var(--green)"/>
      <circle cx="105" cy="727" r="33" fill="var(--step-blue)"/>
    </g>

    <!-- product title pill -->
    <rect x="463" y="85" width="327" height="93" rx="22" fill="var(--green)"/>

    <!-- nutrition table -->
    <g class="nutrition-grid" stroke="#111" stroke-width="3">
      <line x1="510" y1="318" x2="818" y2="318"/>
      <line x1="510" y1="408" x2="818" y2="408"/>
      <line x1="510" y1="448" x2="818" y2="448"/>
      <line x1="510" y1="487" x2="818" y2="487"/>
      <line x1="637" y1="318" x2="637" y2="532"/>
      <line x1="734" y1="318" x2="734" y2="530"/>
    </g>

    <!-- vegetable characters area -->
    <rect x="440" y="565" width="400" height="122" rx="12" fill="url(#harvestTones)" opacity="0.55" role="img" aria-label="Illustration of cartoon vegetables: carrot holding a 100% natural sign, red capsicum, sweet potato, yellow capsicum and beetroot"/>
    <rect x="450" y="689" width="390" height="5" fill="#c9c9cc"/>

    <!-- storage pill -->
    <rect x="555" y="713" width="198" height="32" rx="10" fill="var(--green)" stroke="#1f7f4a" stroke-width="1"/>
  </svg>

  <div class="t brand-name">TOT HARVEST</div>

  <div class="t instructions-title">Instructions :</div>

  <div class="t step-num" style="left:85px; top:466px;">1</div>
  <div class="t step-text" style="top:452px;">pop out the design<br>number of cubes</div>

  <div class="t step-num" style="left:85px; top:586px;">2</div>
  <div class="t step-text" style="left:164px; top:577px;">Heat in the microwave<br>on high for 1-2 minutes</div>

  <div class="t step-num" style="left:85px; top:706px;">3</div>
  <div class="t step-text" style="top:690px;">Stir and allow to cool<br>before serving.</div>

  <div class="t product-name">Sunny Medley</div>
  <div class="t ingredients">pumpkin, beetroot, carrot<br>red capsicum &amp; sweet potato</div>

  <div class="t nutrition-heading">Nutritional Information</div>
  <div class="t nutrition-sub" style="top:287px;">Servings per package 3</div>
  <div class="t nutrition-sub" style="top:298px;">Serving size 2 × 50g cubs (100g)</div>

  <div class="t table-label" style="left:652px; top:331px;">per 50g<br>cube</div>
  <div class="t table-label" style="left:744px; top:331px;">per 100g<br>serving</div>
  <div class="t table-label" style="left:517px; top:371px;">Energy<br>Protein</div>
  <div class="t table-label" style="left:514px; top:413px;">Total fat<br>-Saturated</div>
  <div class="t table-label" style="left:517px; top:451px;">Carbohydrate<br>-Sugars</div>
  <div class="t table-label" style="left:517px; top:490px;">Dietary fibre<br>Sodium</div>

  <div class="t storage">Store in freezer - 18 c.</div>
  <div class="t allergen">Produced on equipment that also processest<br>fish, wheat, and milk products.</div>
  <div class="t claims">No added salt, no added suger<br>100&nbsp;&nbsp; Australian product, NT made, dietitian created</div>
</div>
</body>
</html>
```